Speisekarte für eine Strand-Pizzeria in Kroatien gesucht
Zielgruppe
Eine Pizzeria in einer sehr kleinen Siedlung am Meer in Kroatien, die mehr als nur Pizza anbietet. Zielgruppe sind Touristen und Ferienwohnungs-Besitzer. Die Pizzeria bietet viele verschiedene lokale und internationale Gerichte.
Aufgabenstellung
Bedient wird hauptsächlich draußen auf der Terrasse, so dass die Karten in sehr heller Umgebung im Sommer benutzt werden. Die Karte soll nicht kleiner sein als A5, aber auch nicht größer als A4.
Der Print wird später entweder laminiert oder in einer anderen langliebegen Form sein, damit die Karten mehr als 2 Saisons aushalten.
Die meisten Gerichte sollen in einer sehr schönen Form durch ein Foto dargestellt werden und intelligent angeordnet werden. Einladende Fotos brauchen wir natürlich auch (z.B. Bildarko o.ä). Bei Pizza könnte man eine Ausnahme machen und nicht jede Pizza darstellen, sondern vielleicht eine oder 2 Arten etwas größer darstellen. Eine Karte die wir sehr schön finden sind die von Teig-Kiste, vielleicht kann man sich hier anlehnen.
Die erste Seite bei zugeklappter Karte ist am wichtigsten und soll zum Essen einladen.
Das Logo ist fix (2 Palmen), aber der Schriftzug des Lokals (MELUVERA) steht noch nicht. Hier könnten wir auch eine eigene Schrift gebrauchen, die wiedererkennbar ist, da es 2 Locations gibt.
Die Karte muss in 5 Sprachen verständlich sein (siehe Fotos).
UPDATE: Sollten SIE als Designer nicht alle 5 Sprachen kennen, übernehmen Sie den Text der alten Karte (trotz Fehler). Diese Fehler können wir dann, nach Auswahl des finalen Designs verbessern.
Die aktuelle und katastrophale Karte ist angehängt (bitte beachten, dass hier sehr viele Schreibfehler sind).
UPDATE: Alle Gerichte die auf der alten Karte im Anhang angezeigt werden, sollen in Zukunft auch serviert werden.

```html
<!DOCTYPE html>
<html lang="de">
<head>
<meta charset="utf-8">
<title>Speisekarte – Salat</title>
<link rel="stylesheet" href="https://fonts.googleapis.com/css2?family=Quicksand:wght@400;500&display=swap">
<style>
  :root {
    --backdrop: #efe9e1;
    --paper: #ffffff;
    --paper-shade: #f1f1f1;
    --leaf: #5e944f;
    --leaf-dark: #4f8443;
    --ink: #5f9a4f;
    --band-a: #e3f0df;
    --band-b: #d6e9d1;
    --rule: #e2e2e2;
  }
  * { box-sizing: border-box; margin: 0; padding: 0; }
  html, body { width: 1200px; height: 900px; overflow: hidden; background: var(--backdrop); }
  body { font-family: "Quicksand", sans-serif; color: var(--ink); }

  .menu-spread {
    position: absolute; left: 135px; top: 20px;
    width: 930px; height: 860px;
    display: flex;
    box-shadow: 0 6px 24px rgba(0,0,0,.12);
  }
  .menu-page { width: 465px; height: 100%; display: flex; }

  .price-page {
    position: relative; width: 260px; height: 100%;
    background: linear-gradient(90deg, var(--paper) 60%, var(--paper-shade));
  }
  .menu-page--right .price-page { background: linear-gradient(270deg, var(--paper) 60%, var(--paper-shade)); }

  .section-title {
    position: absolute; top: 40px;
    font-size: 22px; font-weight: 400; letter-spacing: .5px;
  }
  .menu-page--left .section-title { left: 18px; }
  .menu-page--right .section-title { right: 18px; }
  .title-rule { position: absolute; top: 76px; height: 1px; background: var(--rule); }
  .menu-page--left .title-rule { left: 18px; right: 70px; }
  .menu-page--right .title-rule { left: 90px; right: 18px; }

  .size-head { position: absolute; top: 50px; font-size: 12px; width: 26px; text-align: center; }

  .price-band { position: absolute; top: 82px; bottom: 130px; width: 26px; }
  .menu-page--right .price-band { bottom: 40px; }
  .price-band--a { background: var(--band-a); }
  .price-band--b { background: var(--band-b); }

  .dish-list { position: absolute; top: 82px; left: 0; right: 0; }
  .dish-group {
    position: relative; display: flex; align-items: center;
    border-bottom: 1px solid var(--rule);
  }
  .dish-names { list-style: none; font-size: 12.5px; line-height: 15px; }
  .menu-page--left .dish-group { height: 162px; padding-left: 18px; }
  .menu-page--right .dish-group { height: 92px; justify-content: flex-end; padding-right: 18px; }
  .menu-page--right .dish-names { text-align: center; }
  .price { position: absolute; top: 50%; transform: translateY(-50%); width: 26px; text-align: center; font-size: 12px; }

  .photo-page {
    position: relative; width: 205px; height: 100%;
    background: var(--leaf);
  }
  .menu-page--left .photo-page { background: linear-gradient(90deg, var(--leaf), var(--leaf-dark)); }
  .menu-page--right .photo-page { background: linear-gradient(270deg, var(--leaf), var(--leaf-dark)); }
  .food-photo { position: absolute; left: 12px; width: 181px; height: 135px; }
  .food-photo--tomatoes { background: linear-gradient(135deg, #3f7a2c, #c8261a 45%, #e23b24 70%, #e9e2d4); }
  .food-photo--market { background: linear-gradient(135deg, #d94b3a, #8aa94a 35%, #efe8d8 55%, #3a4fa0 80%, #c22b3d); }
  .food-photo--bread-salad { background: linear-gradient(135deg, #e8e4dc, #a9cf6e 35%, #d09a4e 60%, #d8402e 85%); }
  .food-photo--berry-salad { background: linear-gradient(135deg, #2b6fa0, #6ea844 35%, #c9243a 60%, #8fbf4a 85%); }
  .bowl-mark {
    position: absolute; left: 55px; bottom: 25px; width: 95px; height: 75px;
    border-radius: 10px; background: rgba(255,255,255,.06);
  }
</style>
</head>
<body>
<main class="menu-spread">

  <section class="menu-page menu-page--left">
    <div class="price-page">
      <h2 class="section-title">SALAT</h2>
      <div class="title-rule"></div>
      <span class="size-head" style="left:190px">L</span>
      <span class="size-head" style="left:220px">XL</span>
      <div class="price-band price-band--a" style="left:190px"></div>
      <div class="price-band price-band--b" style="left:220px"></div>
      <div class="dish-list">
        <div class="dish-group">
          <ul class="dish-names"><li>Pizza Maragrita</li><li>Pizza Maragrita</li><li>Pizza Maragrita</li><li>Pizza Maragrita</li><li>Pizza Maragrita</li></ul>
          <span class="price" style="left:190px">6€</span><span class="price" style="left:220px">7€</span>
        </div>
        <div class="dish-group">
          <ul class="dish-names"><li>Pizza Maragrita</li><li>Pizza Maragrita</li><li>Pizza Maragrita</li><li>Pizza Maragrita</li><li>Pizza Maragrita</li></ul>
          <span class="price" style="left:190px">6€</span><span class="price" style="left:220px">7€</span>
        </div>
        <div class="dish-group">
          <ul class="dish-names"><li>Pizza Maragrita</li><li>Pizza Maragrita</li><li>Pizza Maragrita</li><li>Pizza Maragrita</li><li>Pizza Maragrita</li></ul>
          <span class="price" style="left:190px">6€</span><span class="price" style="left:220px">7€</span>
        </div>
        <div class="dish-group">
          <ul class="dish-names"><li>Pizza Maragrita</li><li>Pizza Maragrita</li><li>Pizza Maragrita</li><li>Pizza Maragrita</li><li>Pizza Maragrita</li></ul>
          <span class="price" style="left:190px">6€</span><span class="price" style="left:220px">7€</span>
        </div>
      </div>
    </div>
    <div class="photo-page">
      <div class="food-photo food-photo--tomatoes" style="top:90px" role="img" aria-label="Foto: Strauchtomaten mit Basilikum und Knoblauch"></div>
      <div class="food-photo food-photo--market" style="top:265px" role="img" aria-label="Foto: Spargel, Erdbeeren, Beeren und buntes Gemüse"></div>
      <div class="food-photo food-photo--bread-salad" style="top:440px" role="img" aria-label="Foto: Salat mit Croutons, Tomaten und Walnüssen"></div>
      <div class="food-photo food-photo--berry-salad" style="top:615px" role="img" aria-label="Foto: Blattsalat mit Erdbeeren, Beeren und Avocado"></div>
      <div class="bowl-mark" role="img" aria-label="Dezente Zeichnung einer Salatschüssel"></div>
    </div>
  </section>

  <section class="menu-page menu-page--right">
    <div class="photo-page">
      <div class="food-photo food-photo--tomatoes" style="top:90px" role="img" aria-label="Foto: Strauchtomaten mit Basilikum und Knoblauch"></div>
      <div class="food-photo food-photo--market" style="top:265px" role="img" aria-label="Foto: Spargel, Erdbeeren, Beeren und buntes Gemüse"></div>
      <div class="food-photo food-photo--bread-salad" style="top:440px" role="img" aria-label="Foto: Salat mit Croutons, Tomaten und Walnüssen"></div>
      <div class="food-photo food-photo--berry-salad" style="top:615px" role="img" aria-label="Foto: Blattsalat mit Erdbeeren, Beeren und Avocado"></div>
      <div class="bowl-mark" role="img" aria-label="Dezente Zeichnung einer Salatschüssel"></div>
    </div>
    <div class="price-page">
      <h2 class="section-title">SALAT</h2>
      <div class="title-rule"></div>
      <span class="size-head" style="left:6px">XL</span>
      <span class="size-head" style="left:34px">L</span>
      <span class="size-head" style="left:62px">S</span>
      <div class="price-band price-band--b" style="left:6px"></div>
      <div class="price-band price-band--a" style="left:34px"></div>
      <div class="price-band price-band--a" style="left:62px"></div>
      <div class="dish-list">
        <div class="dish-group"><ul class="dish-names"><li>Pizza Maragrita</li><li>Pizza Maragrita</li><li>Pizza Maragrita</li><li>Pizza Maragrita</li><li>Pizza Maragrita</li></ul><span class="price" style="left:6px">7€</span><span class="price" style="left:34px">6€</span><span class="price" style="left:62px">4€</span></div>
        <div class="dish-group"><ul class="dish-names"><li>Pizza Maragrita</li><li>Pizza Maragrita</li><li>Pizza Maragrita</li><li>Pizza Maragrita</li><li>Pizza Maragrita</li></ul><span class="price" style="left:6px">7€</span><span class="price" style="left:34px">6€</span><span class="price" style="left:62px">4€</span></div>
        <div class="dish-group"><ul class="dish-names"><li>Pizza Maragrita</li><li>Pizza Maragrita</li><li>Pizza Maragrita</li><li>Pizza Maragrita</li><li>Pizza Maragrita</li></ul><span class="price" style="left:6px">7€</span><span class="price" style="left:34px">6€</span><span class="price" style="left:62px">4€</span></div>
        <div class="dish-group"><ul class="dish-names"><li>Pizza Maragrita</li><li>Pizza Maragrita</li><li>Pizza Maragrita</li><li>Pizza Maragrita</li><li>Pizza Maragrita</li></ul><span class="price" style="left:6px">7€</span><span class="price" style="left:34px">6€</span><span class="price" style="left:62px">4€</span></div>
        <div class="dish-group"><ul class="dish-names"><li>Pizza Maragrita</li><li>Pizza Maragrita</li><li>Pizza Maragrita</li><li>Pizza Maragrita</li><li>Pizza Maragrita</li></ul><span class="price" style="left:6px">7€</span><span class="price" style="left:34px">6€</span><span class="price" style="left:62px">4€</span></div>
        <div class="dish-group"><ul class="dish-names"><li>Pizza Maragrita</li><li>Pizza Maragrita</li><li>Pizza Maragrita</li><li>Pizza Maragrita</li><li>Pizza Maragrita</li></ul><span class="price" style="left:6px">7€</span><span class="price" style="left:34px">6€</span><span class="price" style="left:62px">4€</span></div>
        <div class="dish-group"><ul class="dish-names"><li>Pizza Maragrita</li><li>Pizza Maragrita</li><li>Pizza Maragrita</li><li>Pizza Maragrita</li><li>Pizza Maragrita</li></ul><span class="price" style="left:6px">7€</span><span class="price" style="left:34px">6€</span><span class="price" style="left:62px">4€</span></div>
        <div class="dish-group" style="border-bottom:none"><ul class="dish-names"><li>Pizza Maragrita</li><li>Pizza Maragrita</li><li>Pizza Maragrita</li><li>Pizza Maragrita</li><li>Pizza Maragrita</li></ul><span class="price" style="left:6px">7€</span><span class="price" style="left:34px">6€</span><span class="price" style="left:62px">4€</span></div>
      </div>
    </div>
  </section>

</main>
</body>
</html>
```